Washroom Services - Flyer Design - to compete with international players

I need a flyer to compete with large international suppliers like Bramwell Sanitary who dominate the washroom services market here in New Zealand. Washroom services include supply and replenishment of air fresheners, soaps, sanitisers, hand towels, toilet paper and sanitary disposal units.
Looking at A4 brochure folded to DLE size (ie in 3) recommendations please if another orientation/size would be better.
Target Market(s)
Businesses with multiple washrooms in one site such as office blocks/towers, municiple buildings, restaurants, gyms.
Requirements
Must have
- Clearbrook Supply Logo, images of the dispensers - nb any other logo currently on a dispenser needs the Clearbrook Supply logo photo shopped onto it.
Nice to have
- Icons to represent different product offerings
Should not have
- Any images of people

```html
<!DOCTYPE html>
<html lang="en">
<head>
<meta charset="utf-8">
<title>Clearbrook Supply – Washroom Services</title>
<link rel="stylesheet" href="https://fonts.googleapis.com/css2?family=Roboto+Condensed:wght@300;400&family=Arimo:wght@400;700&display=swap">
<style>
  :root {
    --brand-blue: #0b5c94;
    --band-text: #ffffff;
    --body-text: #1a1a1a;
    --page: #ffffff;
    --product-light: #f4f5f6;
    --product-mid: #d9dcdf;
    --photo-light: #eeeeec;
    --photo-mid: #c9c9c6;
  }
  * { box-sizing: border-box; margin: 0; padding: 0; }
  html, body { width: 1200px; height: 849px; overflow: hidden; background: var(--page); }
  .flyer {
    position: relative; width: 1200px; height: 849px;
    background: var(--page); color: var(--body-text);
    font-family: "Arimo", Arial, sans-serif;
  }
  .intro-band {
    position: absolute; left: 0; top: 0; width: 1200px; height: 235px;
    background: var(--brand-blue); color: var(--band-text);
    border-bottom: 1px solid #083f66;
  }
  .footer-band {
    position: absolute; left: 0; top: 806px; width: 1200px; height: 43px;
    background: var(--brand-blue);
  }
  .intro {
    position: absolute; top: 38px;
    font-family: "Roboto Condensed", "Arial Narrow", sans-serif;
  }
  .intro h2 { font-weight: 300; font-size: 25px; line-height: 34px; margin-bottom: 8px; letter-spacing: -0.3px; }
  .intro p { font-weight: 300; font-size: 14.8px; line-height: 20.2px; letter-spacing: -0.35px; text-align: justify; }
  .intro--company { left: 40px; width: 340px; }
  .intro--custom { left: 420px; width: 362px; }
  .intro--guarantee { left: 820px; width: 340px; }

  .offer { position: absolute; }
  .offer h3 { font-size: 13.6px; font-weight: 700; line-height: 18px; margin-bottom: 2px; }
  .offer p { font-size: 13.3px; line-height: 16.1px; text-align: justify; }
  .offer .spaced { letter-spacing: 1px; }

  .visual { position: absolute; }
  .visual--photo { background: linear-gradient(160deg, var(--photo-light), var(--photo-mid)); }
  .visual--product {
    background: linear-gradient(100deg, var(--product-mid), var(--product-light) 35%, #ffffff 70%, var(--product-mid));
    border-radius: 10px; box-shadow: 0 1px 3px rgba(0,0,0,0.18);
  }
</style>
</head>
<body>
<div class="flyer">

  <header class="intro-band">
    <section class="intro intro--company">
      <h2>Professional Washroom Service</h2>
      <p>Clearbrook Supply is a New Zealand company with years of experience in the washroom services industry. We have a smart range of washroom dispensers and consumables that will complement your environment at an affordable price.</p>
    </section>
    <section class="intro intro--custom">
      <h2>Customised Service</h2>
      <p>We work with you to ensure that you have the most appropriate washroom solution and service schedule in place. This means that you will have the most relevant level of products and visits customised to your organisation. We can work to a flexible arrangement if your business goes through peaks and troughs with visitors to your bathroom so that you don't pay for products and services you don't require.</p>
    </section>
    <section class="intro intro--guarantee">
      <h2>Service Guarantee</h2>
      <p>Our team are professionals in the washroom services industry and we guarantee the quality of our work with our service guarantee. We are reliable and ensure that all installations, service calls and maintenance are delivered on time, every time.</p>
    </section>
  </header>

  <section class="offer" style="left:40px; top:260px; width:340px;">
    <h3>Sanitary Disposal Units</h3>
    <p>The Cubicle Slim is a new and innovative slim line sanitary disposal system. It's available in automatic or manual units. The Cubicle Slim takes up minimal space in each cubicle and is wall mounted for easy cleaning underneath.</p>
  </section>
  <div class="visual visual--photo" style="left:55px; top:374px; width:138px; height:126px;" role="img" aria-label="Slim sanitary disposal unit mounted beside a toilet"></div>
  <div class="visual visual--photo" style="left:222px; top:374px; width:145px; height:126px;" role="img" aria-label="Sanitary disposal unit with lid opening automatically"></div>

  <section class="offer" style="left:40px; top:529px; width:340px;">
    <h3>Air Fresheners</h3>
    <p>Our range of air fresheners include both traditional automatic spray units as well as passive aerosol free units. The range of fragrance and odour neutralisers are extensive and will be matched to best suit your environment.</p>
  </section>
  <div class="visual visual--product" style="left:78px; top:640px; width:65px; height:134px;" role="img" aria-label="White automatic spray air freshener unit"></div>
  <div class="visual visual--product" style="left:250px; top:654px; width:60px; height:116px;" role="img" aria-label="Passive aerosol free air freshener unit"></div>

  <section class="offer" style="left:420px; top:261px; width:270px;">
    <h3>Soap Dispensers</h3>
    <p>Soap dispensers are available in standard flowing soap and foaming hand soap varieties. We will make recommendations on the most appropriate soap for your washroom users.</p>
  </section>
  <div class="visual visual--product" style="left:704px; top:268px; width:70px; height:102px;" role="img" aria-label="White wall mounted soap dispenser"></div>

  <section class="offer" style="left:420px; top:392px; width:270px;">
    <h3>Hand Sanitisers</h3>
    <p>Our hand sanitiser units can be used in washrooms, hallways or office situations. You can opt for alcohol free or alcohol based sanitiser solutions.</p>
  </section>
  <div class="visual visual--product" style="left:704px; top:402px; width:70px; height:110px;" role="img" aria-label="White wall mounted hand sanitiser unit"></div>

  <section class="offer" style="left:420px; top:532px; width:270px;">
    <h3>WC/Urinal Sanitisers</h3>
    <p>By fitting a system that pumps a sanitising solution directly into toilets and urinals you will reduce odours and prevent pipe blockages.</p>
  </section>
  <div class="visual visual--product" style="left:724px; top:546px; width:58px; height:116px;" role="img" aria-label="White WC and urinal sanitiser pump unit"></div>

  <section class="offer" style="left:420px; top:668px; width:197px;">
    <h3>WC Seat Sanitising Solutions</h3>
    <p>For peace of mind for your <span class="spaced">bathroom visitors we can</span> provide WC sanitisers. These are available in either a solution form that is administered via <span class="spaced">toilet tissue or a dispenser</span> loaded with wet wipes.</p>
  </section>
  <div class="visual visual--product" style="left:634px; top:702px; width:53px; height:78px;" role="img" aria-label="White seat sanitiser solution dispenser"></div>
  <div class="visual visual--product" style="left:722px; top:692px; width:52px; height:84px; background:linear-gradient(100deg,#d9dcdf,#f4f5f6 20%,#f0a640 35%,#f0a640 60%,#f4f5f6 75%,#d9dcdf);" role="img" aria-label="Seat sanitiser wet wipe dispenser with orange window"></div>

  <section class="offer" style="left:820px; top:260px; width:252px;">
    <h3>Toilet Tissue</h3>
    <p>We will work with you to identify the most <span class="spaced">appropriate toilet paper solution</span> depending on the traffic through your site. This could be jumbo rolls, mini jumbos or individual toilet rolls. Don't worry about the terminology – it's our job to come up with the right solution.</p>
  </section>
  <div class="visual visual--photo" style="left:1080px; top:265px; width:80px; height:71px;" role="img" aria-label="Stack of toilet paper rolls"></div>
  <div class="visual visual--photo" style="left:1086px; top:344px; width:70px; height:36px; border-radius:18px;" role="img" aria-label="Jumbo toilet roll"></div>

  <section class="offer" style="left:820px; top:410px; width:250px;">
    <h3>Hand Towels</h3>
    <p>Paper hand towels are available in a range of different types depending on your requirements. As a complementary offering or alternative option we can provide you with a high speed hand dryer.</p>
  </section>
  <div class="visual visual--photo" style="left:1098px; top:410px; width:42px; height:48px;" role="img" aria-label="Folded paper hand towels"></div>
  <div class="visual visual--product" style="left:1092px; top:464px; width:48px; height:94px;" role="img" aria-label="White high speed hand dryer"></div>

  <section class="offer" style="left:820px; top:544px; width:250px;">
    <h3>Baby Change Station</h3>
    <p>If you anticipate having babies in your bathroom, then our baby change station is an economical and safe option that you can purchase outright.</p>
  </section>
  <div class="visual visual--product" style="left:1076px; top:582px; width:76px; height:42px; border-radius:6px;" role="img" aria-label="Fold down baby change station"></div>

  <section class="offer" style="left:820px; top:653px; width:340px;">
    <h3>Other Options</h3>
    <p>Our range of washroom dispensers, fixtures and consumables go far beyond the ones we have outlined here. At all times we will ensure that we get a full understanding of your bathroom visitors so that we can make the most appropriate recommendations. If your circumstances change, we will change out products and services as you require.</p>
  </section>

  <footer class="footer-band"></footer>
</div>
</body>
</html>
```